Bref créative
Business Cards + Stationary for IT Company
Datavertiza
Simple
Rodrigo Baltierra
Presidente & CEO
Oriente 275 No. 512-408
Industrial Montoro
04710, Tlalmivara, D.F.
rb@datavertiza.com
www.datavertiza.com
Please include the Zentrik Logos on the back or front depending of design and distribution
Company logo with commercial name
Company logo with no commercial name
Back card Zentrik partner logo
Back card Certified specialist
Enterprise Premier Partner
This image shall be in the front in a smaller size than company logo.

```html
<!DOCTYPE html>
<html lang="es">
<head>
<meta charset="utf-8">
<title>Datavertiza — Tarjetas de presentación</title>
<link rel="stylesheet" href="https://fonts.googleapis.com/css2?family=Arimo:wght@400;700&display=swap">
<style>
  :root {
    --backdrop: #e9eaec;
    --card: #f8f8f9;
    --brand-blue: #2f8fd6;
    --brand-blue-deep: #1f72b8;
    --swoosh-grey: #66696e;
    --text-grey: #5d6066;
    --text-dark: #3d4045;
    --badge-grey: #d9dbde;
    --white: #ffffff;
  }
  * { margin: 0; padding: 0; box-sizing: border-box; }
  html, body {
    width: 1200px;
    height: 838px;
    overflow: hidden;
    background: var(--backdrop);
    font-family: "Arimo", Arial, sans-serif;
  }
  .card {
    position: absolute;
    left: 260px;
    width: 680px;
    height: 388px;
    background: var(--card);
    box-shadow: 0 8px 24px rgba(0,0,0,0.14);
    overflow: hidden;
  }
  .card--back { top: 22px; }
  .card--front { top: 428px; }

  /* Back side */
  .back-holder {
    position: absolute;
    right: 30px;
    top: 26px;
    text-align: right;
  }
  .back-holder .holder-name {
    font-size: 17px;
    font-weight: 700;
    color: var(--brand-blue);
  }
  .back-holder .holder-title {
    font-size: 10px;
    color: var(--text-grey);
    margin-top: 2px;
  }
  .back-lockup {
    position: absolute;
    left: 0;
    right: 0;
    top: 160px;
    display: flex;
    justify-content: center;
    align-items: center;
    gap: 14px;
  }
  .back-lockup .brand-square { width: 34px; height: 34px; }
  .back-lockup .brand-name { font-size: 48px; }
  .partner-badge {
    position: absolute;
    right: 30px;
    bottom: 26px;
    width: 96px;
    height: 34px;
    border-radius: 4px;
    background: var(--badge-grey);
  }

  /* Shared brand */
  .brand-square { display: block; background: var(--brand-blue); }
  .brand-name { font-weight: 400; color: var(--text-dark); }

  /* Front side */
  .card-graphics { position: absolute; inset: 0; }
  .front-lockup {
    position: absolute;
    left: 38px;
    top: 206px;
    display: flex;
    align-items: center;
    gap: 9px;
  }
  .front-lockup .brand-square { width: 20px; height: 20px; }
  .front-lockup .brand-name { font-size: 32px; }
  .front-holder {
    position: absolute;
    right: 30px;
    top: 168px;
    text-align: right;
    color: var(--white);
  }
  .front-holder .holder-name { font-size: 17px; font-weight: 700; }
  .front-holder .holder-title { font-size: 10px; margin-top: 2px; }
  .address {
    position: absolute;
    left: 38px;
    top: 282px;
    font-style: normal;
    font-size: 13px;
    line-height: 19px;
    color: var(--text-grey);
  }
  .contact-divider {
    position: absolute;
    left: 252px;
    top: 282px;
    width: 1.5px;
    height: 58px;
    background: var(--text-grey);
  }
  .contact-list {
    position: absolute;
    left: 262px;
    top: 282px;
    list-style: none;
    font-size: 13px;
    line-height: 19px;
    color: var(--text-grey);
  }
  .contact-list li { display: flex; align-items: center; gap: 6px; }
  .contact-icon { width: 11px; height: 11px; fill: var(--text-grey); }
  .website {
    position: absolute;
    left: 262px;
    top: 344px;
    font-size: 13px;
    color: var(--text-grey);
  }
</style>
</head>
<body>
  <article class="card card--back">
    <div class="back-holder">
      <p class="holder-name">Rodrigo Baltierra</p>
      <p class="holder-title">Presidente &amp; CEO</p>
    </div>
    <div class="back-lockup">
      <span class="brand-square"></span>
      <span class="brand-name">datavertiza</span>
    </div>
    <div class="partner-badge" role="img" aria-label="Zentrik partner badge"></div>
  </article>

  <article class="card card--front">
    <svg class="card-graphics" viewBox="0 0 680 388" width="680" height="388" aria-hidden="true">
      <path fill="var(--brand-blue)" d="M0,165 C140,130 270,60 370,0 L680,0 L680,250 C560,252 430,215 310,194 C210,178 100,176 0,196 Z"/>
      <path fill="var(--brand-blue-deep)" opacity="0.35" d="M60,184 C150,170 230,172 310,186 C430,207 560,244 680,242 L680,250 C560,252 430,215 310,194 C210,178 130,178 60,184 Z"/>
      <path fill="none" stroke="var(--swoosh-grey)" stroke-width="8" d="M262,214 C400,214 520,262 600,272 C640,277 665,276 684,273"/>
    </svg>

    <div class="front-lockup">
      <span class="brand-square"></span>
      <span class="brand-name">datavertiza</span>
    </div>

    <div class="front-holder">
      <p class="holder-name">Rodrigo Baltierra</p>
      <p class="holder-title">Presidente &amp; CEO</p>
    </div>

    <address class="address">
      Oriente 275 No. 512-408<br>
      Industrial Montoro<br>
      04710, Tlalmivara, D.F.
    </address>

    <div class="contact-divider"></div>

    <ul class="contact-list">
      <li>
        <svg class="contact-icon" viewBox="0 0 24 24"><path d="M6.6 10.8c1.4 2.8 3.8 5.1 6.6 6.6l2.2-2.2c.3-.3.7-.4 1-.2 1.1.4 2.3.6 3.6.6.6 0 1 .4 1 1V20c0 .6-.4 1-1 1C10.6 21 3 13.4 3 4c0-.6.4-1 1-1h3.5c.6 0 1 .4 1 1 0 1.3.2 2.5.6 3.6.1.3 0 .7-.2 1z"/></svg>
        +52 55 4387-1290
      </li>
      <li>
        <svg class="contact-icon" viewBox="0 0 24 24"><path d="M7 2h10a2 2 0 0 1 2 2v16a2 2 0 0 1-2 2H7a2 2 0 0 1-2-2V4a2 2 0 0 1 2-2zm0 3v12h10V5zm5 13.5a1 1 0 1 0 0 2 1 1 0 0 0 0-2z"/></svg>
        772-518-6047
      </li>
      <li>
        <svg class="contact-icon" viewBox="0 0 24 24"><path d="M3 5h18a1 1 0 0 1 1 1v12a1 1 0 0 1-1 1H3a1 1 0 0 1-1-1V6a1 1 0 0 1 1-1zm1 2.2V17h16V7.2l-8 5.3z M5 7l7 4.6L19 7z"/></svg>
        rb@datavertiza.com
      </li>
    </ul>

    <p class="website">www.datavertiza.com</p>
  </article>
</body>
</html>
```